Web Design Project (Mente Lumo)

We are going to do a therapy template to a psychologist. The site already exists, adress: www.mentelumo.net. So, its a total redesign job. I'm from Brazil, the language is PT-BR, so I'm gonna translate what you think be necessary. You can use the current structure from the website as a base to the new design. Check this template to see what I usually like: http://www.layoutkestrel.com/demo/51907.html
Updates

I'm waiting for new creative designs. The 'structure' image is just for 'pb'.

Requirements
Must have
• We need a modern menu, it should use a cool font style and make some kind of effect and little noise when the user pass over with the mouse (FLASH/HTML 5). The main page must emphasize the fact that we offer online treatment, like a picture or frame saying "Online Treatment, click here". It must also show the therapist picture and her name. The colors need to pass a tranquility feeling. The clinic telephone must always be present, doesn't matter which page the user is. The website must adapt to any resolution above 1024x768, crossbrowsing and accept javascript (I'll use www.slotvira.com, so its necessary embed code)
Nice to have
• I would appreciate if there was some kind of slow background animation, passing behind the text using the transparency.
Should not have
• Can't take too long to load, and won't have news or blog

```html
<!DOCTYPE html>
<html lang="pt-BR">
<head>
<meta charset="utf-8">
<title>Mente Lumo — Terapia Cognitiva</title>
<link rel="stylesheet" href="https://fonts.googleapis.com/css2?family=Arimo:wght@400;700&display=swap">
<style>
:root{
  --header:#05424c;
  --header-band:#3f8e97;
  --hero:#d3e4e8;
  --content:#b1c8cc;
  --footer:#34939f;
  --ink:#0a4650;
  --ink-soft:#1d5863;
  --nav:#c9d7d9;
  --green:#7cbf1c;
  --panel:#044550;
  --white:#ffffff;
}
*{margin:0;padding:0;box-sizing:border-box}
html,body{width:1200px;height:1000px;overflow:hidden}
body{font-family:"Arimo",Arial,sans-serif;background:var(--content);position:relative;color:var(--ink)}
.abs{position:absolute}
.nowrap{white-space:nowrap}

.site-header{left:0;top:0;width:1200px;height:135px;background:linear-gradient(135deg,#06464f,#043c45)}
.header-band{left:0;top:135px;width:1200px;height:15px;background:var(--header-band)}
.brand{left:128px;top:55px;display:flex;align-items:center;gap:12px}
.brand-mark{width:32px;height:32px;border-radius:50%;background:#7fb7b0}
.brand-name{font-size:27px;font-weight:700;color:#cfe0c8;letter-spacing:.3px}

.main-nav a{position:absolute;top:87px;font-size:14.5px;font-weight:700;color:var(--nav);text-decoration:none;letter-spacing:.2px}
.main-nav .nav-home{left:404px;top:62px;width:66px;height:62px;border-radius:4px;background:linear-gradient(#9ad43a,#5e9e17);color:var(--white);text-align:center;line-height:64px;box-shadow:0 1px 2px rgba(0,0,0,.3)}
.nav-indicator{left:408px;top:134px;width:60px;height:4px;border-radius:2px;background:#d9eef0}

.hero{left:0;top:150px;width:1200px;height:333px;background:var(--hero)}
.hero-rule{left:0;top:483px;width:1200px;height:3px;background:#f2f8f9}
.hero-title{left:115px;top:210px;font-size:36px;font-weight:700;color:var(--ink)}
.hero-text{left:116px;top:272px;font-size:18px;line-height:24.5px;color:var(--ink)}
.btn{display:block;border-radius:4px;background:linear-gradient(#9ad43a,#4f8c12);border:1px solid #3f7410;color:#eef6e3;font-weight:700;text-align:center;text-decoration:none;letter-spacing:1px}
.hero-btn{left:514px;top:417px;width:149px;height:38px;line-height:36px;font-size:17px}
.hero-figure{left:740px;top:178px;width:330px;height:319px;border-radius:12px;background:linear-gradient(165deg,#dfe8ea 0%,#e3c4b0 35%,#c98a66 60%,#f1ede8 100%)}

.profile{left:113px;top:549px;width:340px;height:217px;border-radius:3px;background:var(--panel)}
.profile-photo{left:15px;top:19px;width:130px;height:149px;border-radius:3px;background:linear-gradient(#9a9a9a,#5c5c5c)}
.profile-title{left:159px;top:17px;font-size:30px;font-weight:700;color:var(--green)}
.profile-text{left:159px;top:56px;font-size:12.3px;line-height:14.4px;color:var(--white)}
.profile-name{left:29px;top:185px;font-size:13.5px;font-weight:700;color:var(--white)}

.about-title{left:483px;top:562px;font-size:30px;font-weight:700;color:var(--ink)}
.about-text{left:483px;top:604px;font-size:12.2px;line-height:14.4px;color:var(--ink-soft)}
.about-btn{left:684px;top:745px;width:85px;height:28px;line-height:26px;font-size:11.5px}

.phone-box{left:808px;top:541px;width:262px;height:38px;border:2px solid var(--panel);border-radius:4px;background:var(--white);display:flex;align-items:center}
.phone-icon{width:38px;height:100%;background:var(--panel);display:flex;align-items:center;justify-content:center}
.phone-number{flex:1;text-align:right;padding-right:12px;font-size:24px;font-weight:700;color:var(--ink)}

.online-banner{left:808px;top:599px;width:262px;height:69px;border-radius:3px;overflow:hidden;background:linear-gradient(100deg,#0c5a62,#2a7a80 60%,#bfcfd0)}
.online-photo{left:160px;top:0;width:102px;height:69px;background:linear-gradient(90deg,rgba(233,236,236,0),#e6e9e9 30%,#c9b7aa)}
.online-line1{left:15px;top:7px;font-size:23px;font-weight:700;color:#8fd03a}
.online-line2{left:15px;top:37px;font-size:23px;font-weight:700;color:var(--white)}

.map-title{left:807px;top:688px;font-size:24px;font-weight:700;color:var(--ink)}
.map-area{left:805px;top:720px;width:266px;height:98px;border:2px solid var(--panel);border-radius:4px;background:linear-gradient(120deg,#ece7da,#e4e2dc 50%,#f1e48a)}

.site-footer{left:0;top:843px;width:1200px;height:157px;background:var(--footer)}
.footer-info{left:77px;top:861px;font-size:12.5px;line-height:14.5px;color:var(--white)}
.footer-nav a{position:absolute;top:864px;font-size:11px;font-weight:700;color:var(--white);text-decoration:none}
</style>
</head>
<body>
<header class="abs site-header"></header>
<div class="abs header-band"></div>

<div class="abs brand">
  <span class="brand-mark"></span>
  <span class="brand-name">Mente Lumo</span>
</div>

<nav class="main-nav">
  <a class="nav-home" href="#">HOME</a>
  <a href="#" style="left:486px">TRATAMENTOS</a>
  <a href="#" style="left:616px">PERGUNTAS</a>
  <a href="#" style="left:732px">CONSULTÓRIO</a>
  <a href="#" style="left:867px">LOCALIZAÇÃO</a>
  <a href="#" style="left:999px">CONTATO</a>
</nav>
<div class="abs nav-indicator"></div>

<section class="abs hero"></section>
<div class="abs hero-rule"></div>
<h1 class="abs hero-title">O que terapia cognitiva?</h1>
<p class="abs hero-text nowrap">A Terapia Cognitiva tem como método a interpretação de processos e<br>conteúdos mentais (as cognições), e sua influência na vida cotidiana.<br>O comportamento e a emoção vêm depois do processamento<br>cognitivo. É vital conhecermos nossos pensamentos para termos<br>controle sobre eles, e assim podemos: nutri-los, expandi-los,...</p>
<a class="abs btn hero-btn" href="#">READ MORE</a>
<div class="abs hero-figure" role="img" aria-label="Illustration of a thoughtful woman with a thought bubble reading 'its vital to know your thoughts!'"></div>

<article class="abs profile">
  <div class="abs profile-photo" role="img" aria-label="Portrait photo of the therapist"></div>
  <h2 class="abs profile-title">Profil</h2>
  <p class="abs profile-text nowrap">Jujubes jelly beans pastry<br>cake biscuit jujubes oat cake.<br>Candy canes candy canes<br>topping lemon drops liquorice.<br>Faworki chocolate bar cookie<br>tart powder tootsie roll<br>macaroon liquorice.<br>Candy canes candy canes</p>
  <p class="abs profile-name">Name Surname</p>
</article>

<h2 class="abs about-title">About us</h2>
<p class="abs about-text nowrap">Jujubes jelly beans pastry cake biscuit jujubes oat<br>cake. Candy canes candy canes topping lemon drops<br>liquorice. Faworki chocolate bar cookie tart powder<br>tootsie roll macaroon liquorice.<br>Jujubes jelly beans pastry cake biscuit jujubes oat<br>cake. Candy canes candy canes topping lemon drops<br>liquorice. Faworki chocolate bar cookie tart powder<br>tootsie roll macaroon liquorice.Jujubes jelly beans<br>pastry cake biscuit jujubes oat cake. Candy canes</p>
<a class="abs btn about-btn" href="#">READ MORE</a>

<div class="abs phone-box">
  <span class="phone-icon">
    <svg width="22" height="26" viewBox="0 0 24 24" aria-hidden="true"><path fill="#ffffff" d="M6.6 10.8a15.1 15.1 0 0 0 6.6 6.6l2.2-2.2c.3-.3.7-.4 1-.2 1.1.4 2.3.6 3.6.6.6 0 1 .4 1 1V20c0 .6-.4 1-1 1A17 17 0 0 1 3 4c0-.6.4-1 1-1h3.5c.6 0 1 .4 1 1 0 1.3.2 2.5.6 3.6.1.3 0 .7-.2 1z"/></svg>
  </span>
  <span class="phone-number">(11) 4072-5390</span>
</div>

<a class="abs online-banner" href="#">
  <span class="abs online-photo" role="img" aria-label="Photo of a woman using a laptop"></span>
  <span class="abs online-line1">ON LINE</span>
  <span class="abs online-line2">treament</span>
</a>

<h2 class="abs map-title">Map</h2>
<div class="abs map-area" role="img" aria-label="Street map of the clinic location"></div>

<footer class="abs site-footer"></footer>
<p class="abs footer-info nowrap">Rua das Palmeiras Altas, 142, 5º andar, Sala 31 - Centro - Vila Serena, SP<br>contato@mentelumo.net<br>Copyright © 2012 - Todos os direitos reservados</p>
<nav class="footer-nav">
  <a href="#" style="left:587px">HOME</a>
  <a href="#" style="left:642px">TRATAMENTOS</a>
  <a href="#" style="left:744px">PERGUNTAS</a>
  <a href="#" style="left:835px">CONSULTÓRIO</a>
  <a href="#" style="left:938px">LOCALIZAÇÃO</a>
  <a href="#" style="left:1040px">CONTATO</a>
</nav>
</body>
</html>
```